Visitenkarten-Design für Mit Ruhe ans Ziel
Zielgruppe
Ich biete Menschen, die in ihrem Beruf hohen Stressbelastungen ausgesetzt sind, schnelle und wirksame Hilfe. Sie können bei mir lernen, langfristig ohne Stress in ihrem Job erfolgreich zu sein.
Mein Angebot nennt sich „Mit Ruhe ans Ziel“. Es besteht aus drei Bausteinen, einem wissenschaftlichem Stresstest, intensiven Kleingruppen-Workshops und individuellem Einzelcoaching.
So kann ich flexibel für jeden die passende Lösungsstrategie zur Stressbewältigung anbieten.
Aufgabenstellung
Farbwelt des Logos Mit Ruhe ans Ziel berücksichtigen
Persönlichen Daten/Adressdaten auf der Vorderseite:
Marlene Wuttkamp
Personal/Business Coach
Stressmanagement-Trainerin
Beraterin für KALMIX Stressprävention by Dornacker®
Lindgrubenweg 7
10435 Berlin
Tel: (030) 41276380
Mobil: (0173) 2864159
Email: info@mit-ruhe-ans-ziel.example
Text auf der Rückseite:
Mit Ruhe ans Ziel:
Wissenschaftlicher Stresstest KALMIX
Intensive Kleingruppen-Workshops
Individuelles Coaching
www.mit-ruhe-ans-ziel.example

```html
<!DOCTYPE html>
<html lang="de">
<head>
<meta charset="utf-8">
<title>Mit Ruhe ans Ziel – Visitenkarten</title>
<link href="https://fonts.googleapis.com/css2?family=Hind:wght@300;400;500;600;700&display=swap" rel="stylesheet">
<style>
  :root {
    --green: #86bb44;
    --berry: #b4667c;
    --ink: #2e2e2e;
    --grey: #7d7d80;
    --paper: #ffffff;
    --board: #f1f2f4;
  }
  * { margin: 0; padding: 0; box-sizing: border-box; }
  html, body { width: 848px; height: 1200px; overflow: hidden; background: var(--board); }
  body { position: relative; font-family: "Hind", Arial, sans-serif; color: var(--ink); }

  .brand-mark {
    position: absolute; top: 92px; left: 0; width: 848px;
    display: flex; justify-content: center; align-items: center; gap: 10px;
  }
  .brand-dot { width: 12px; height: 12px; border-radius: 50%; background: var(--green); }
  .brand-name { font-size: 34px; font-weight: 600; color: var(--berry); letter-spacing: -0.3px; line-height: 1; }

  .card {
    position: absolute; width: 373px; height: 242px; overflow: hidden;
    box-shadow: 6px 8px 14px rgba(0,0,0,0.18);
  }
  .card--front { left: 42px; top: 232px; background: var(--paper); border-left: 4px solid var(--green); }
  .card--back { left: 442px; top: 234px; background: var(--green); }

  .card-logo { position: absolute; display: flex; align-items: center; gap: 7px; }
  .card-logo .brand-dot { width: 9px; height: 9px; }
  .card-logo .brand-name { font-size: 25px; }
  .card--front .card-logo { left: 55px; top: 30px; }
  .card--back .card-logo { left: 68px; top: 30px; }
  .card--back .brand-name { color: var(--paper); }
  .card--back .brand-dot { background: var(--paper); }

  .holder { position: absolute; left: 56px; top: 90px; font-size: 10.5px; font-weight: 600; }
  .roles { position: absolute; left: 56px; top: 107px; list-style: none; font-size: 10px; line-height: 14.6px; }
  .roles li::before, .offer li::before {
    content: ""; display: inline-block; width: 4px; height: 4px; border-radius: 50%;
    background: var(--berry); margin-right: 5px; vertical-align: 2px;
  }
  .address { position: absolute; left: 40px; top: 195px; font-size: 10px; line-height: 14px; }
  .divider { position: absolute; left: 173px; top: 178px; width: 1.5px; height: 64px; background: var(--berry); }
  .contact { position: absolute; left: 184px; top: 181px; list-style: none; font-size: 10px; line-height: 14px; }
  .contact li { display: flex; align-items: center; gap: 6px; }
  .contact svg { width: 9px; height: 9px; fill: var(--berry); flex: none; }

  .back-arc { position: absolute; left: 0; top: 0; }
  .offer { position: absolute; left: 96px; top: 108px; list-style: none; font-size: 10px; line-height: 14.6px; font-weight: 300; color: var(--paper); }
  .offer li::before { background: var(--berry); }
  .web { position: absolute; left: 90px; top: 205px; font-size: 12px; font-weight: 600; color: var(--paper); letter-spacing: 0.3px; }
</style>
</head>
<body>
  <header class="brand-mark">
    <span class="brand-dot"></span>
    <span class="brand-name">Mit Ruhe ans Ziel</span>
  </header>

  <section class="card card--front" aria-label="Vorderseite">
    <div class="card-logo"><span class="brand-dot"></span><span class="brand-name">Mit Ruhe ans Ziel</span></div>
    <p class="holder">Marlene Wuttkamp</p>
    <ul class="roles">
      <li>Personal/Business Coach</li>
      <li>Stressmanagement-Trainerin</li>
      <li>Beraterin für KALMIX Stressprävention by Dornacker®</li>
    </ul>
    <p class="address">Lindgrubenweg 7<br>10435 Berlin</p>
    <span class="divider"></span>
    <ul class="contact">
      <li><svg viewBox="0 0 10 10"><path d="M2 0.5 L3.6 0.5 L4.2 2.8 L3 3.6 Q4 5.9 6.4 7 L7.2 5.8 L9.5 6.4 L9.5 8 Q9.5 9.5 8 9.5 Q1 9 0.5 2 Q0.5 0.5 2 0.5Z"/></svg>(030) 41276380</li>
      <li><svg viewBox="0 0 10 10"><path d="M2.5 0.5 H7.5 V9.5 H2.5Z M3.3 1.5 V7.6 H6.7 V1.5Z M4.6 8.1 H5.4 V8.9 H4.6Z"/></svg>(0173) 2864159</li>
      <li><svg viewBox="0 0 10 10"><path d="M0.5 2 H9.5 V8.5 H0.5Z M1 2.4 L5 5.6 L9 2.4" stroke="#fff" stroke-width="0.8"/></svg>info@mit-ruhe-ans-ziel.example</li>
    </ul>
  </section>

  <section class="card card--back" aria-label="Rückseite">
    <svg class="back-arc" width="373" height="242" viewBox="0 0 373 242" aria-hidden="true">
      <path d="M160 0 Q40 40 5 242 L150 242 Q60 170 80 95 Q100 30 170 0Z" fill="var(--berry)"/>
    </svg>
    <div class="card-logo"><span class="brand-dot"></span><span class="brand-name">Mit Ruhe ans Ziel</span></div>
    <ul class="offer">
      <li>Wissenschaftlicher Stresstest KALMIX</li>
      <li>Intensive Kleingruppen-Workshops</li>
      <li>Individuelles Coaching</li>
    </ul>
    <p class="web">www.mit-ruhe-ans-ziel.example</p>
  </section>
</body>
</html>
```